Launch Invite for LUMEN in hand-drawn chalk style

Looking for an invitation for the launch of LUMEN a creative marketing collaborative founded by Gloria Pembrook. We are a marketing consultancy firm. We are fun, quirky and do things a little different. The launch party will have a silent auction to benefit the charity Guarding Our Prairies. The auction will be a photography show feature local photographers with the theme of Texas natural resources and wildlife. Event will be Wednesday, May 22 from 6:30 to 9:30p at Harlow Gallery located at 514 North 9th, Austin, Texas

Please see the attached verbiage for invite text. Words in bold indicate importance.

We want a chalkboard art invitation similar to the style of Mira Koslowe. So just a black chalkboard background with white chalk text.

http://www.mirakoslowe-example.com/chalk/

Target Market(s)

freinds, family, small business owners, influencers, non-profits

Industry/Entity Type

Charity

Requirements
Must have
• Love the style of the Nora Belden piece on Mira's Website.
Or nagging image or wedding couples image.
chalkboard invite with chalk text
fun, looks like its going to be a good time.
Nice to have
• Highlight lumen, date, time, location, charity

```html
<!DOCTYPE html>
<html lang="en">
<head>
<meta charset="utf-8">
<title>LUMEN Launch Invitation</title>
<link rel="stylesheet" href="https://fonts.googleapis.com/css2?family=Anton&family=Dosis:wght@600;700&family=Mulish:wght@800&family=Passion+One:wght@700&family=Play:wght@400;700&family=Poiret+One&family=Rye&display=swap">
<style>
  :root {
    --page: #ffffff;
    --board: #050505;
    --board-edge: #141414;
    --chalk: #f4f4f2;
    --chalk-soft: #d9d9d6;
    --ink: #2a2a2a;
    --badge-gold: #b59a57;
  }
  html, body {
    margin: 0;
    padding: 0;
    width: 880px;
    height: 1200px;
    overflow: hidden;
    background: var(--page);
  }
  .sheet {
    position: relative;
    width: 880px;
    height: 1200px;
  }
  .size-label {
    position: absolute;
    left: 83px;
    top: 68px;
    margin: 0;
    font-family: "Times New Roman", Times, serif;
    font-size: 17px;
    letter-spacing: 1.5px;
    color: var(--ink);
  }
  .invite {
    position: absolute;
    left: 0;
    top: 0;
    width: 880px;
    height: 1200px;
  }
  .chalk { fill: var(--chalk); }
  .chalk-line { fill: none; stroke: var(--chalk); stroke-linecap: round; }
  .greeting { font-family: "Mulish", sans-serif; font-weight: 800; font-size: 48px; letter-spacing: 1px; }
  .headline { font-family: "Anton", sans-serif; font-size: 64px; letter-spacing: 2px; }
  .tagline { font-family: "Play", sans-serif; font-size: 21px; letter-spacing: 0.5px; }
  .founded { font-family: "Poiret One", sans-serif; font-size: 36px; }
  .founder { font-family: "Poiret One", sans-serif; font-size: 46px; }
  .services { font-family: "Play", sans-serif; font-size: 19px; letter-spacing: 0.4px; }
  .celebrate { font-family: "Rye", serif; font-size: 56px; letter-spacing: 3px; }
  .event-detail { font-family: "Passion One", sans-serif; font-weight: 700; font-size: 30px; letter-spacing: 1.5px; }
  .auction-title { font-family: "Dosis", sans-serif; font-weight: 700; font-size: 21px; }
  .charity-note { font-family: "Dosis", sans-serif; font-weight: 600; font-size: 15px; }
  .footer-info { font-family: "Dosis", sans-serif; font-weight: 600; font-size: 15.5px; }
  .partner-name { font-family: "Dosis", sans-serif; font-weight: 700; font-size: 11px; fill: var(--ink); }
  .partner-tile { fill: var(--page); }
  .seal-tile { fill: var(--page); }
  .seal-shape { fill: none; stroke: #9a9a9a; stroke-width: 2; }
</style>
</head>
<body>
<main class="sheet">
  <p class="size-label">SIZE : 5.8″ X 8.4″</p>

  <svg class="invite" viewBox="0 0 880 1200" xmlns="http://www.w3.org/2000/svg">
    <defs>
      <radialGradient id="board-tone" cx="50%" cy="45%" r="70%">
        <stop offset="0%" stop-color="var(--board-edge)"/>
        <stop offset="100%" stop-color="var(--board)"/>
      </radialGradient>
      <path id="headline-arc" d="M 140 322 Q 442 130 752 330"/>
      <path id="celebrate-arc" d="M 196 725 Q 442 600 700 728"/>
    </defs>

    <!-- chalkboard -->
    <rect class="board" x="83" y="95" width="714" height="1030" fill="url(#board-tone)"/>

    <!-- side rails -->
    <g class="side-rails chalk-line" stroke-width="1.6">
      <line x1="110" y1="140" x2="110" y2="1090"/>
      <line x1="117" y1="140" x2="117" y2="1090"/>
      <line x1="763" y1="140" x2="763" y2="1090"/>
      <line x1="770" y1="140" x2="770" y2="1090"/>
    </g>

    <!-- frame curves -->
    <g class="frame-curves chalk-line" stroke-width="2.4">
      <path d="M 185 470 Q 150 420 190 378 Q 260 330 440 326 Q 620 330 690 378 Q 730 420 695 470"/>
      <path d="M 190 840 Q 160 900 195 960 Q 230 1000 300 990 Q 380 980 440 1010 Q 500 980 580 990 Q 650 1000 685 960 Q 720 900 690 840"/>
    </g>

    <!-- small dividers -->
    <g class="dividers chalk-line" stroke-width="2">
      <path d="M 350 515 Q 440 500 530 515"/>
      <path d="M 395 843 Q 440 835 485 843"/>
    </g>

    <!-- header -->
    <text class="chalk greeting" x="440" y="160" text-anchor="middle">HELLO AUSTIN!</text>
    <text class="chalk headline">
      <textPath href="#headline-arc" startOffset="50%" text-anchor="middle">INTRODUCING LUMEN</textPath>
    </text>

    <!-- founder block -->
    <text class="chalk tagline" x="440" y="397" text-anchor="middle">CREATIVE MARKETING COLLABORATIVE</text>
    <text class="chalk founded" x="440" y="446" text-anchor="middle">FOUNDED BY</text>
    <text class="chalk founder" x="440" y="494" text-anchor="middle">GLORIA PEMBROOK</text>

    <!-- services -->
    <g class="chalk services" text-anchor="middle">
      <text x="440" y="571">CRAFTING BRANDS FOR SMALL BUSINESSES</text>
      <text x="440" y="595">MARKETING, NON-PROFITS, STRATEGY, START UPS</text>
      <text x="440" y="619">DESIGN, SOCIAL MEDIA, PR</text>
    </g>

    <!-- celebrate -->
    <text class="chalk celebrate">
      <textPath href="#celebrate-arc" startOffset="50%" text-anchor="middle">CELEBRATE</textPath>
    </text>

    <!-- event details -->
    <g class="chalk event-detail">
      <g text-anchor="end">
        <text x="406" y="764">WEDNESDAY</text>
        <text x="406" y="794">MAY 22</text>
        <text x="406" y="824">6:30 TO 9:30</text>
      </g>
      <g text-anchor="start">
        <text x="442" y="764">HARLOW GALLERY</text>
        <text x="442" y="794">514 NORTH 9TH</text>
        <text x="442" y="824">AUSTIN, TEXAS</text>
      </g>
    </g>
    <g class="chalk detail-dots">
      <circle cx="424" cy="744" r="2.6"/><circle cx="424" cy="753" r="2.6"/>
      <circle cx="424" cy="762" r="2.6"/><circle cx="424" cy="771" r="2.6"/>
      <circle cx="424" cy="780" r="2.6"/><circle cx="424" cy="789" r="2.6"/>
      <circle cx="424" cy="798" r="2.6"/><circle cx="424" cy="807" r="2.6"/>
      <circle cx="424" cy="816" r="2.6"/>
    </g>

    <!-- auction -->
    <g class="chalk auction-title" text-anchor="middle">
      <text x="440" y="880">TEXAS PHOTOGRAPHY GALLERY</text>
      <text x="440" y="904">SILENT AUCTION BENEFITING</text>
    </g>
    <g class="chalk charity-note" text-anchor="middle">
      <text x="440" y="930">STARTED BY HELEN MARSH TO SPUR CONSERVATION</text>
      <text x="440" y="949">EFFORTS THAT BENEFIT COMMUNITIES, BUILD ON THE SUCCESS</text>
      <text x="440" y="968">OF OTHERS, &amp; INSPIRE ALL TEXANS TO JOIN IN.</text>
    </g>

    <!-- partner marks -->
    <g class="partner">
      <rect class="partner-tile" x="155" y="1016" width="78" height="78"/>
      <text class="partner-name" x="194" y="1052" text-anchor="middle">GUARDING OUR</text>
      <text class="partner-name" x="194" y="1066" text-anchor="middle">PRAIRIES</text>
    </g>
    <g class="state-badge">
      <rect class="seal-tile" x="649" y="1016" width="78" height="78"/>
      <circle class="seal-shape" cx="688" cy="1055" r="31"/>
    </g>

    <!-- footer -->
    <g class="chalk footer-info" text-anchor="middle">
      <text x="440" y="1082">INFO : GLORIA@LUMENGROUP.COM</text>
      <text x="440" y="1101">ATTIRE : KEEP AUSTIN STYLISH</text>
    </g>
  </svg>
</main>
</body>
</html>
```